Progressive Architecture and Urban Planning Studio - Stationery Design

The Kestrel Collective: a small boutique Architectural and Urban Planning Studio based in Natal/ RN, Brazil, about to open branches in South Africa and West Africa, established to provide high quality, innovative design and personal client service for projects worldwide. Our approach to Architecture: Minimal - Less is More, so to speak, but with an edge! Strive to produce "clean" projects - stripped of all that can be stripped, no excesses. Got our Logo right here with Pixel Harbor, and hope to do the same with our stationery (were informed that includes business cards, letterhead and envelopes). Since we'll be using two clour schemes, we want at least one using a black background (business card). We'll also allow manipulation of our logo if it helps the final design. Good Luck!

Font styles to use
Other font styles liked:
• Nexa

Colors

Designer to choose colors to be used in the design.

Requirements
Must have
• Business Cards/ Letterheads with the following address:
Rua Olavo Pereira 2741, Vale Dourado, Natal/RN
Should be able to edit it.

```html
<!DOCTYPE html>
<html lang="en">
<head>
<meta charset="utf-8">
<title>The Kestrel Collective – Business Cards</title>
<link rel="stylesheet" href="https://fonts.googleapis.com/css2?family=Montserrat:wght@300;400&family=Allura&family=Roboto+Condensed:wght@400;700&display=swap">
<style>
  :root {
    --surface: #e4e8e9;
    --paper: #ffffff;
    --ink: #111111;
    --night: #050505;
    --accent: #e0080b;
    --accent-deep: #b50608;
    --mist: #f2f2f2;
  }
  * { box-sizing: border-box; margin: 0; padding: 0; }
  html, body {
    width: 1200px;
    height: 848px;
    overflow: hidden;
  }
  body {
    background: var(--surface);
    display: flex;
    align-items: center;
    justify-content: center;
    gap: 60px;
  }
  .card {
    position: relative;
    width: 500px;
    height: 290px;
    overflow: hidden;
    box-shadow: 0 10px 28px rgba(0,0,0,0.18);
  }
  .card--front { background: var(--paper); color: var(--ink); }
  .card--back { background: var(--night); color: var(--paper); }
  .card__band {
    position: absolute;
    left: 0; right: 0; bottom: 0;
    height: 22px;
    background: linear-gradient(180deg, var(--accent-deep), var(--accent));
  }
  .wordmark {
    display: flex;
    align-items: center;
    gap: 14px;
    font-family: "Montserrat", sans-serif;
    font-weight: 300;
    letter-spacing: 0.32em;
    text-transform: uppercase;
    white-space: nowrap;
  }
  .wordmark__dot {
    width: 26px; height: 26px;
    border-radius: 50%;
    flex: none;
  }
  .card--front .wordmark {
    position: absolute;
    top: 34px; left: 32px;
    font-size: 17px;
  }
  .card--front .wordmark__dot { background: var(--accent); }
  .card--back .wordmark {
    position: absolute;
    top: 118px; left: 50%;
    transform: translateX(-50%);
    font-size: 16px;
    color: var(--mist);
  }
  .card--back .wordmark__dot { background: var(--mist); }
  .role {
    position: absolute;
    top: 88px; left: 0; right: 0;
    text-align: center;
  }
  .role__title {
    font-family: "Allura", cursive;
    font-size: 64px;
    line-height: 1;
  }
  .role__level {
    display: block;
    font-family: "Roboto Condensed", sans-serif;
    font-size: 17px;
    text-align: right;
    padding-right: 92px;
    margin-top: -8px;
  }
  .contact {
    position: absolute;
    right: 30px; bottom: 40px;
    font-family: "Roboto Condensed", sans-serif;
    font-size: 15px;
    line-height: 1.35;
    text-align: right;
  }
  .contact__label { color: var(--accent); font-weight: 700; }
</style>
</head>
<body>
  <section class="card card--front" aria-label="Business card front">
    <div class="wordmark"><span class="wordmark__dot"></span>The Kestrel Collective</div>
    <div class="role">
      <p class="role__title">Project Owner</p>
      <span class="role__level">director</span>
    </div>
    <address class="contact">
      <p>Rua Olavo Pereira 2741, Vale Dourado, Natal/RN</p>
      <p><span class="contact__label">T</span> 00 000 0000 &nbsp;<span class="contact__label">F</span> 00 000 0000</p>
    </address>
    <div class="card__band"></div>
  </section>

  <section class="card card--back" aria-label="Business card back">
    <div class="wordmark"><span class="wordmark__dot"></span>The Kestrel Collective</div>
    <div class="card__band"></div>
  </section>
</body>
</html>
```